Email signature

I have an email signature, card and letter head and I would like the colours darker and more distinctive and I would like the contact details to be bigger and or easier to read as they are hard to read at the moment. The arrow watermark is fine I think.

Logo Text

CORVELL GUARD PTY LTD

Requirements
Nice to have
• The yellow type colour with the grey is good and I would like to retain that, but it looks washed out and too light on the screen. I like the arrows and I like the watermark arrows as well and I would like to retain the basic design.

```html
<!DOCTYPE html>
<html lang="en">
<head>
<meta charset="utf-8">
<title>Corvell Guard – Business Card</title>
<link rel="stylesheet" href="https://fonts.googleapis.com/css2?family=Arimo:wght@400&display=swap">
<style>
  :root {
    --paper: #ffffff;
    --brand-yellow: #e8b400;
    --brand-grey: #4f4f4f;
  }
  html, body {
    margin: 0;
    padding: 0;
    overflow: hidden;
    background: var(--paper);
  }
  .card {
    position: relative;
    width: 1200px;
    height: 1000px;
    background: var(--paper);
    font-family: "Arimo", Arial, sans-serif;
    font-weight: 400;
    overflow: hidden;
  }
  .card p, .card h1, .card h2 { margin: 0; }
  .wordmark {
    position: absolute;
    left: 160px;
    top: 118px;
    width: 898px;
    color: var(--brand-grey);
    font-weight: 400;
    line-height: 1;
  }
  .wordmark__name {
    display: block;
    font-size: 82px;
    letter-spacing: 2px;
  }
  .wordmark__suffix {
    display: block;
    text-align: right;
    font-size: 55px;
    letter-spacing: 3px;
    margin-top: 12px;
  }
  .person {
    position: absolute;
    right: 142px;
    top: 474px;
    text-align: right;
    line-height: 1;
  }
  .person__name {
    font-size: 48px;
    font-weight: 400;
    color: var(--brand-grey);
    letter-spacing: 1px;
  }
  .person__role {
    margin-top: 13px !important;
    font-size: 47px;
    color: var(--brand-yellow);
  }
  .contact {
    position: absolute;
    font-size: 33px;
    line-height: 1;
    color: var(--brand-grey);
    white-space: nowrap;
    letter-spacing: 0.5px;
  }
  .contact__label {
    color: var(--brand-yellow);
    display: inline-block;
  }
  .contact--phone { right: 142px; top: 769px; word-spacing: 10px; }
  .contact--phone .contact__label { margin-right: 50px; word-spacing: 0; }
  .contact--email { left: 160px; top: 827px; }
  .contact--email .contact__label { margin-right: 44px; }
  .contact--web { right: 142px; top: 827px; }
  .contact--web .contact__label { margin-right: 24px; }
</style>
</head>
<body>
  <main class="card">
    <h1 class="wordmark">
      <span class="wordmark__name">CORVELL GUARD</span>
      <span class="wordmark__suffix">PTY LTD</span>
    </h1>

    <section class="person">
      <h2 class="person__name">DALE MORGAN</h2>
      <p class="person__role">DIRECTOR</p>
    </section>

    <p class="contact contact--phone"><span class="contact__label">PH</span>0412 608 294</p>
    <p class="contact contact--email"><span class="contact__label">E</span>dale@corvellguard.net.au</p>
    <p class="contact contact--web"><span class="contact__label">W</span>www.corvellguard.net.au</p>
  </main>
</body>
</html>
```